RLT Nursing Care

I am a registered nurse with a private nursing care service.
We provide the following care;
Registered Nursing, Palliative Nursing, personal care, dementia repite, day respite , overnight respite, domestic assistance, welfare checks, and transport.
In the community, our service is brochured by service providers and we also supply to private clients.

Target Market(s)

Aged care, disabled clients, dementia clients in the community

Industry/Entity Type

Nurse

Font styles to use
Sans Serif

Colors
6b449b
e44699
b868aa

Requirements
Must have
• Contact: Marlene Hobbs - Registered Nurse
PO Box 482 Dubbo
0437 215 608
Nice to have
• A soft caring picture feature

```html
<!DOCTYPE html>
<html lang="en">
<head>
<meta charset="utf-8">
<title>Marlene Hobbs – Registered Nurse</title>
<link rel="stylesheet" href="https://fonts.googleapis.com/css2?family=Roboto:wght@300;700&family=Roboto+Condensed:wght@300;400;500;700&display=swap">
<style>
  :root {
    --stage: #110f0f;
    --purple: #6b449b;
    --band: #67479a;
    --pink: #e44699;
    --mauve: #b868aa;
    --lilac: #cdb7dc;
    --blush: #f3d3e6;
    --blush-soft: #fbeef5;
    --coat: #f8f6f8;
    --white: #ffffff;
  }
  * { margin: 0; padding: 0; box-sizing: border-box; }
  html, body {
    width: 1200px; height: 1200px; overflow: hidden;
    background: var(--stage);
  }
  .flyer {
    position: absolute; left: 147px; top: 248px;
    width: 906px; height: 702px; overflow: hidden;
    background:
      linear-gradient(180deg, rgba(255,255,255,0) 0%, rgba(255,255,255,.35) 30%, rgba(255,255,255,0) 55%, rgba(255,255,255,.3) 80%),
      linear-gradient(90deg, var(--blush) 0%, var(--blush-soft) 45%, var(--blush) 70%, var(--blush-soft) 100%);
  }
  .feature-photo {
    position: absolute; left: 393px; top: 0; width: 513px; height: 702px;
    background:
      linear-gradient(90deg, rgba(251,238,245,1) 0%, rgba(251,238,245,0) 22%),
      radial-gradient(ellipse 150px 330px at 66% 48%, rgba(107,68,155,.55) 0%, rgba(184,104,170,.25) 55%, rgba(255,255,255,0) 100%),
      radial-gradient(ellipse 420px 520px at 60% 60%, var(--white) 0%, var(--coat) 60%, rgba(236,226,236,1) 100%),
      var(--coat);
  }
  .name {
    position: absolute; left: 58px; top: 68px;
    font-family: "Roboto", Arial, sans-serif; color: var(--purple);
    font-size: 68px; line-height: 70px; letter-spacing: -1px;
  }
  .name .first { display: block; font-weight: 300; }
  .name .last { display: block; font-weight: 700; }
  .intro, .community {
    position: absolute; left: 58px; width: 360px;
    font-family: "Roboto Condensed", Arial, sans-serif; font-weight: 300;
    color: var(--pink); font-size: 21px; line-height: 31px;
  }
  .intro { top: 228px; }
  .community { top: 507px; }
  .services {
    position: absolute; left: 58px; top: 337px; list-style: none;
    font-family: "Roboto Condensed", Arial, sans-serif; font-weight: 400;
    color: var(--purple); font-size: 22px; line-height: 31px;
  }
  .contact-band {
    position: absolute; left: 0; top: 0; width: 906px; height: 702px;
  }
  .contact-line {
    position: absolute; left: 0; top: 641px; width: 906px; text-align: center;
    font-family: "Roboto Condensed", Arial, sans-serif; font-weight: 500;
    color: var(--white); font-size: 23px; line-height: 28px;
  }
</style>
</head>
<body>
  <main class="flyer">
    <div class="feature-photo" role="img" aria-label="Photo of a nurse in a white coat and purple scrubs with a stethoscope, arms crossed"></div>

    <h1 class="name"><span class="first">Marlene</span><span class="last">Hobbs</span></h1>

    <p class="intro">I am a registered nurse with a private<br>nursing care service. We provide<br>the following care;</p>

    <ul class="services">
      <li>• Registered Nursing • Palliative Nursing</li>
      <li>• Personal care • Dementia repite</li>
      <li>• Day respite • Overnight respite</li>
      <li>• Domestic assistance</li>
      <li>• Welfare checks • Transport</li>
    </ul>

    <p class="community">In the community, our service is<br>brochured by service providers and<br>we also supply to private clients.</p>

    <svg class="contact-band" viewBox="0 0 906 702" aria-hidden="true">
      <path d="M0 652 Q453 582 906 652 L906 702 L0 702 Z" fill="var(--band)"/>
    </svg>
    <p class="contact-line">Registered Nurse • PO Box 482 Dubbo • 0437 215 608</p>
  </main>
</body>
</html>
```